Harbor Petroleum Business Cards

I would like to design some options for about 10 sets of double sided business cards for our team with a raised logo with a Silver glossy finished logo. We are a privately funded upstream Oil & Gas producer drilling vertical wells in Central Oklahoma with a long term production (ROI driven) strategy that we implement through an annual drilling program. We are focused on a shallow / vertical / long life / low decline strategy. We are based in downtown Tulsa Oklahoma. I have attached a sample business card and a picture of our hallway logo which we would like to replicate on the business cards.

Target Market(s)

SEC Accredited Investors and other Oil & Gas Operators

Industry/Entity Type

Upstream Oil & Gas

Contact Information for Business Card

You can see the sample photo attached, but email / website / address / direct phone / Cell Phone / Name / Title / Fax

Font styles to use
Other font styles liked:
• Felix Titling

Colors
0054AA
0677BA
7BADD7
CADEEF
E8F1F8

Requirements
Must have
• Glossy raised logo
Nice to have
• Possibly a new logo.
Should not have
• No Greens /

```html
<!DOCTYPE html>
<html lang="en">
<head>
<meta charset="utf-8">
<title>Harbor Petroleum Business Cards</title>
<link href="https://fonts.googleapis.com/css2?family=Tinos:wght@400;700&display=swap" rel="stylesheet">
<style>
  :root {
    --backdrop: #d9dadc;
    --card-dark: #232427;
    --card-light: #ffffff;
    --accent-grey: #6f6e6c;
    --ink-grey: #5b5b5d;
    --ink-light: #f2f2f2;
    --silver: #9a9ca1;
  }
  * { margin: 0; padding: 0; box-sizing: border-box; }
  html, body { width: 1200px; height: 780px; overflow: hidden; }
  body {
    background: var(--backdrop);
    font-family: "Tinos", "Times New Roman", serif;
    position: relative;
  }
  .card {
    position: absolute;
    top: 235px;
    width: 540px;
    height: 309px;
    overflow: hidden;
    box-shadow: 0 6px 16px rgba(0,0,0,0.25);
  }
  .card-front { left: 40px; background: var(--card-light); }
  .card-back { left: 620px; background: var(--card-dark); }

  .front-wave { position: absolute; inset: 0; width: 540px; height: 309px; }

  .front-brand {
    position: absolute;
    top: 22px;
    right: 30px;
    display: flex;
    align-items: center;
    gap: 8px;
    color: var(--ink-grey);
    font-size: 14px;
    font-weight: 400;
    letter-spacing: 1px;
    line-height: 16px;
    text-transform: uppercase;
    white-space: nowrap;
  }
  .brand-dot {
    width: 11px; height: 11px; border-radius: 50%;
    background: var(--ink-grey);
    flex: none;
  }

  .holder {
    position: absolute;
    top: 52px;
    left: 28px;
    color: var(--ink-grey);
    text-transform: uppercase;
    white-space: nowrap;
  }
  .holder-name { font-size: 19px; line-height: 22px; font-weight: 700; letter-spacing: 1px; }
  .holder-title { font-size: 12px; line-height: 15px; letter-spacing: 0.5px; margin-top: 3px; }

  .contact {
    position: absolute;
    left: 28px;
    top: 170px;
    color: var(--ink-light);
    font-size: 13px;
    line-height: 15px;
    white-space: nowrap;
  }
  .address { text-transform: uppercase; margin-bottom: 6px; }
  .contact-list { list-style: none; }
  .contact-list li { display: flex; align-items: center; gap: 7px; }
  .contact-icon { width: 11px; height: 11px; flex: none; }

  .back-brand {
    position: absolute;
    inset: 0;
    display: flex;
    align-items: center;
    justify-content: center;
    gap: 14px;
    color: var(--silver);
    font-size: 30px;
    font-weight: 400;
    letter-spacing: 2px;
    text-transform: uppercase;
    white-space: nowrap;
  }
  .back-brand .brand-dot { width: 22px; height: 22px; background: var(--silver); }
</style>
</head>
<body>

<section class="card card-front" aria-label="Business card front">
  <svg class="front-wave" viewBox="0 0 540 309" aria-hidden="true">
    <path d="M0,140 C60,118 130,120 220,128 C340,138 440,120 540,70 L540,309 L0,309 Z" fill="var(--accent-grey)"/>
    <path d="M0,152 C60,130 130,132 220,140 C340,150 440,136 540,88 L540,309 L0,309 Z" fill="var(--card-dark)"/>
  </svg>

  <div class="front-brand"><span class="brand-dot"></span>Harbor Petroleum, LLC</div>

  <div class="holder">
    <div class="holder-name">Dalton R. Whitcomb, CPL</div>
    <div class="holder-title">Executive Vice President<br>Land, Legal &amp; Business Development</div>
  </div>

  <div class="contact">
    <div class="address">220 South Main St Suite 900<br>Tulsa, OK 74103</div>
    <ul class="contact-list">
      <li>
        <svg class="contact-icon" viewBox="0 0 12 12"><path d="M3 1 L5 3.5 L4 4.8 C4.8 6.4 5.8 7.4 7.2 8 L8.5 7 L11 9 L9.6 11 C5 10.5 1.5 7 1 2.4 Z" fill="#fff"/></svg>
        555-010-2234 (Direct)
      </li>
      <li>
        <svg class="contact-icon" viewBox="0 0 12 12"><rect x="3" y="0.5" width="6" height="11" rx="1" fill="none" stroke="#fff"/><rect x="4.3" y="2" width="3.4" height="6" fill="#fff"/></svg>
        555-014-7391 (Cell)
      </li>
      <li>
        <svg class="contact-icon" viewBox="0 0 12 12"><rect x="3" y="0.5" width="6" height="4" fill="#fff"/><rect x="1" y="4.5" width="10" height="5" fill="#fff"/><rect x="3" y="9" width="6" height="2.5" fill="#fff"/></svg>
        555-017-6830 (Fax)
      </li>
      <li>
        <svg class="contact-icon" viewBox="0 0 12 12"><rect x="0.5" y="2" width="11" height="8" fill="#fff"/><path d="M0.5 2 L6 6.5 L11.5 2" fill="none" stroke="var(--card-dark)"/></svg>
        DRW@HPTulsa.com
      </li>
      <li>
        <svg class="contact-icon" viewBox="0 0 12 12"><circle cx="6" cy="6" r="5.5" fill="#fff"/><path d="M0.5 6 H11.5 M6 0.5 C3.5 3 3.5 9 6 11.5 M6 0.5 C8.5 3 8.5 9 6 11.5" fill="none" stroke="var(--card-dark)" stroke-width="0.8"/></svg>
        www.HarborPetroleumLLC.com
      </li>
    </ul>
  </div>
</section>

<section class="card card-back" aria-label="Business card back">
  <div class="back-brand"><span class="brand-dot"></span>Harbor Petroleum, LLC</div>
</section>

</body>
</html>
```